Lindenhof Wissensportal - Redesign
Die Seite http://www.lindenhof-wissensportal.de soll einem kompletten neu designed werden. Der Inhalt soll so übernommen werden. Auf der Startseite soll ein Blog inegriert werden. Typische Features wie Zeitachsenarchiv, Tagclouds, letzte Kommentare und Social Media Links sollen intelligent integriert werden. Alle Menüpunkte sollen als Themenvorschläge auf der Wesite mit entsprechenden Bildern integriert werden.
Beispiel: Menüpunkt Top Emittenten. Auf der Wesite wird dann beispielsweise ein kleiner Kasten mit Headline "Wer sind die Besten?" inetgriert. Im Kasten ist ein ansprechends Bild und ein kurzer Text: "Die bseten Emittenten finden Sie hier!"
Ein intelligentes Cockpit soll den User auf jeder Seite begleiten. Hier wird der Newsletter angeboten und die Social Media Links verpackt. Darüber hinaus eine E-Mail zur Kontaktaufnahme.
Als Leitfarben sehen wir folgende Kombinationsmöglichkeiten:
a. Grau - Orange
b. Grau - Froschgrün
c. Graubraun - Orange
Bitte berücksichtigen Sie, dass unsere Besucher zwischen 40 und 70 Jahre alt sind.
Die späterr Programmierung soll in Wordpress stattfinden!
Bei weiteren Fragen wenden Sie sich gerne an mich.
Viel Erfolg!

```html
<!DOCTYPE html>
<html lang="de">
<head>
<meta charset="utf-8">
<title>Lindenhof Wissensportal</title>
<link href="https://fonts.googleapis.com/css2?family=Arimo:wght@400;700&display=swap" rel="stylesheet">
<style>
:root{
  --green:#7cc300;
  --green-dark:#62a000;
  --nav-dark:#2f2f2f;
  --nav-light:#5a5a5a;
  --text:#333;
  --muted:#8a8a8a;
  --panel:#e8e8e8;
  --line:#d6d6d6;
  --white:#fff;
}
*{box-sizing:border-box;margin:0;padding:0}
html,body{width:1200px;height:2282px;overflow:hidden;background:var(--white)}
body{position:relative;font-family:"Arimo",Arial,sans-serif;color:var(--text);font-size:14.4px;line-height:19.2px}
a{color:var(--green)}
.abs{position:absolute}

/* navigation */
.main-nav{left:20px;top:16px;width:1160px;height:53px;background:linear-gradient(#5c5c5c,#2c2c2c);display:flex;align-items:center}
.main-nav a{color:#fff;text-decoration:none;font-size:17px;text-transform:uppercase;height:53px;line-height:53px;position:relative;white-space:nowrap}
.main-nav .active{background:var(--green);color:#1c3300;width:95px;text-align:center}
.main-nav .item{flex:1;text-align:center}
.main-nav .item+.item::before{content:"";position:absolute;left:0;top:16px;height:22px;border-left:1px solid #999}

/* header */
.site-header{left:20px;top:69px;width:1160px;height:263px;background:var(--white)}
.header-photo{position:absolute;left:0;top:0;width:382px;height:263px;background:linear-gradient(135deg,#c79a7c,#8c5e45 55%,#e7e2dc)}
.site-title{position:absolute;left:372px;top:96px;font-weight:700;color:var(--green);font-size:56px;line-height:62px;white-space:nowrap}
.site-tagline{position:absolute;right:28px;top:176px;font-size:28px;line-height:34px;color:#222;white-space:nowrap}
.breadcrumb{left:17px;top:332px;width:1167px;height:24px;background:var(--green);color:#fff;font-size:12px;line-height:24px;padding-left:22px;box-shadow:0 3px 6px rgba(0,0,0,.15)}
.breadcrumb a{color:#fff}

/* welcome */
.welcome{left:32px;top:380px;width:1100px}
.section-title{font-weight:700;color:var(--green);font-size:19px;line-height:24px}
.welcome-cols{display:flex;gap:88px;margin-top:18px}
.welcome-cols p{width:512px;font-size:14.4px}

/* feature boxes */
.features{left:16px;top:526px;width:1168px;height:104px;display:flex;gap:3px}
.feature{flex:1;background:linear-gradient(#f3f3f3,#e2e2e2);position:relative;padding:16px 0 0 24px}
.feature .thumb{position:absolute;left:24px;top:10px;width:54px;height:30px;background:linear-gradient(#cfcfcf,#8d8d8d)}
.feature h3{font-size:17px;color:var(--green);margin-left:74px;line-height:22px}
.feature p{font-size:14.4px;line-height:17px;margin-top:4px;width:300px}
.feature:nth-child(2){padding-left:65px}.feature:nth-child(2) .thumb{left:68px}
.feature:nth-child(3){padding-left:78px}.feature:nth-child(3) .thumb{left:80px}

/* divider */
.column-divider{left:799px;top:650px;height:1476px;border-left:1px solid var(--line)}

/* intro */
.intro{left:32px;top:686px;width:700px}
.intro h2{font-size:24px;color:var(--green);line-height:30px}
.intro .lead{margin-top:4px}
.rule-links{list-style:none;margin-top:18px}
.rule-links li{font-size:15.6px;color:var(--green);height:44.5px}
.eggs{left:408px;top:798px;width:216px;height:102px;border-radius:50%/45%;background:radial-gradient(circle at 40% 35%,#f4d77a,#b88a1e 60%,#f2f2f2 80%)}

/* share bar */
.share-bar{left:26px;width:719px;height:32px;background:#efefef;border-bottom:1px solid var(--line);display:flex;font-size:12px;color:#777;align-items:center}
.share-bar span{display:flex;align-items:center;gap:6px;padding:0 14px;height:32px;border-right:1px solid var(--line)}
.share-bar i{font-style:normal;background:#fff;border:1px solid #ccc;padding:0 6px;line-height:16px;font-size:11px}
.share-bar svg{width:14px;height:14px}

.blog-pill{left:26px;top:1003px;width:90px;height:34px;border-radius:17px;background:var(--green);color:#fff;font-weight:700;font-size:21px;line-height:34px;text-align:center}

/* posts */
.post{left:32px;width:690px}
.post-head{display:flex;align-items:center;gap:14px;height:44px}
.date-badge{width:40px;height:44px;background:var(--green);color:#fff;text-align:center;font-weight:700;line-height:1}
.date-badge b{display:block;font-size:16px;padding-top:5px}
.date-badge small{display:block;font-size:7px}
.post-head h2{font-size:21.6px;color:var(--green)}
.post-body{margin-top:7px}
.post-image{float:left;width:209px;height:154px;border:1px solid #aaa;margin:0 11px 6px 0;background:radial-gradient(circle at 50% 55%,#f3cf5a,#c79414 55%,#fff 75%)}
.post-body p{font-size:14.4px;line-height:19.2px}
.post-body p+p{margin-top:19.2px}
.post-body .more{display:block;margin-top:19.2px;clear:both}

/* sidebar */
.sidebar{left:818px;width:346px}
.side-title{font-size:16.5px;font-weight:700;color:#222;border-bottom:1px solid var(--green);padding-bottom:4px}
.newsletter-box{left:818px;top:691px;width:346px;height:168px;background:linear-gradient(#e9e9e9,#d9d9d9);padding:18px 24px;font-size:14.4px;line-height:19px}
.newsletter-box label{display:block;margin-top:12px}
.newsletter-box .field{height:28px;background:#fff;border:1px solid #aaa;margin-top:2px}
.newsletter-box .send{position:absolute;right:24px;top:132px;width:98px;height:28px;border-radius:14px;background:linear-gradient(#a4e038,#5fa000);color:#fff;text-align:center;line-height:28px;font-size:15px}
.social-link{left:818px;width:346px;height:52px;background:linear-gradient(#f2f2f2,#d9d9d9);display:flex;align-items:center;gap:34px;padding-left:18px;font-size:17px;color:#444;letter-spacing:.5px;text-decoration:none}
.social-link svg{width:38px;height:38px}

.tag-cloud{left:818px;top:1236px;width:346px;color:var(--muted);line-height:34px;font-size:14px;border-bottom:1px solid var(--green);padding-bottom:6px}
.tag-cloud .xs{font-size:8px}.tag-cloud .s{font-size:14px}.tag-cloud .m{font-size:20px;color:#777}.tag-cloud .l{font-size:26px}.tag-cloud .xl{font-size:32px}

.archive{left:823px;top:1570px;width:340px;display:grid;grid-template-columns:180px 160px;row-gap:10.8px;font-size:14.4px;list-style:none}

/* footer */
.site-footer{left:17px;top:2136px;width:1167px;height:28px;background:#555;color:#fff;font-size:14.4px;line-height:28px;padding-left:16px}
.site-footer a{color:#fff;text-decoration:none}
.bookmark-badge{position:absolute;right:26px;top:6px;width:148px;height:17px;background:#fff;border:1px solid #ccc}
</style>
</head>
<body>

<nav class="main-nav abs">
  <a class="active" href="#">Start</a>
  <a class="item" href="#">Warum Fonds?</a>
  <a class="item" href="#">Sektoren</a>
  <a class="item" href="#">Top Emittenten</a>
  <a class="item" href="#">Ratings</a>
  <a class="item" href="#">Kaufen ohne Agio</a>
</nav>

<header class="site-header abs">
  <div class="header-photo" role="img" aria-label="Porträtfoto des Ratgeber-Autors"></div>
  <div class="site-title">Lindenhof Wissensportal</div>
  <div class="site-tagline">...gut beraten anlegen.</div>
</header>
<div class="breadcrumb abs">Sie befinden sich auf der <a href="#">Startseite</a></div>

<section class="welcome abs">
  <h1 class="section-title">Herzlich Willkommen bei Lindenhof Wissensportal</h1>
  <div class="welcome-cols">
    <p>Lorem ipsum dolor sit amet, consetetur sadipscing elitr, sed diam nonumy eirmod tempor invidunt ut labore et dolore magna aliquyam erat, sed diam voluptua. At vero eos et accusam et justo duo dolores et ea rebum. Stet clita kasd gubergren, no sea takimata sanctus est Lorem ipsum dolor sit amet. Lore</p>
    <p>Lorem ipsum dolor sit amet, consetetur sadipscing elitr, sed diam nonumy eirmod tempor invidunt ut labore et dolore magna aliquyam erat, sed diam voluptua. At vero eos et accusam et justo duo dolores et ea rebum. Stet clita kasd gubergren, no sea takimata sanctus est Lorem ipsum dolor sit amet. Lore</p>
  </div>
</section>

<section class="features abs">
  <div class="feature"><div class="thumb" role="img" aria-label="Bild einer silbernen Krone"></div><h3>TOP EMMITTENTEN</h3><p>Lorem ipsum dolor sit amet, consetetur sadipscing elitr, sed diam nonumy eirmod tempor invidunt ut labore <a href="#">mehr Infos</a></p></div>
  <div class="feature"><div class="thumb" role="img" aria-label="Bild eines Fragezeichens aus Figuren"></div><h3>WARUM FONDS?</h3><p>Lorem ipsum dolor sit amet, consetetur sadipscing elitr, sed diam nonumy eirmod tempor invidunt ut labore <a href="#">mehr Infos</a></p></div>
  <div class="feature"><div class="thumb" role="img" aria-label="Bild von Sektorenkarten"></div><h3>SEKTOREN</h3><p>Lorem ipsum dolor sit amet, consetetur sadipscing elitr, sed diam nonumy eirmod tempor invidunt ut labore <a href="#">mehr Infos</a></p></div>
</section>

<div class="column-divider abs"></div>

<section class="intro abs">
  <h2>Sie wollen die besten geschlossenen Fonds finden?</h2>
  <p class="lead">Dann folgen Sie meinem Ratgeber zu den besten geschlossenen Fonds.</p>
  <ul class="rule-links">
    <li>Die 3 goldenen Regeln bei Immobilienfonds</li>
    <li>Die 3 goldenen Regeln Flugzeugfonds</li>
    <li>Die 3 goldenen Regeln bei Schiffsfonds</li>
    <li>Die 3 goldenen Regeln bei Umweltfonds</li>
  </ul>
</section>
<div class="eggs abs" role="img" aria-label="Foto von drei goldenen Eiern"></div>

<div class="share-bar abs" style="top:954px">
  <span><svg viewBox="0 0 14 14"><ellipse cx="7" cy="6" rx="6" ry="4.5" fill="#f2d27a"/></svg>Kommentieren <i>0</i></span>
  <span><svg viewBox="0 0 14 14"><circle cx="7" cy="7" r="5" fill="#6fb3de"/></svg>Zwitschern <i>12</i></span>
  <span><svg viewBox="0 0 14 14"><rect x="1" y="1" width="12" height="12" fill="#4a6ea8"/></svg>Teilen <i>0</i></span>
</div>

<div class="blog-pill abs">BLOG</div>

<article class="post abs" style="top:1073px">
  <div class="post-head"><div class="date-badge"><b>15</b><small>NOV<br>2009</small></div><h2>Sie wollen die besten geschlossenen Fonds finden?</h2></div>
  <div class="post-body">
    <div class="post-image" role="img" aria-label="Bild einer goldenen Krone"></div>
    <p>AIFM Richtlinie für geschlossene Fonds:<br>Auf Nimmerwiedersehen grauer Kapitalmarkt!<br>von Dr. Martin Albrecht am 15. Dezember 2010<br>Die AIFM Richtlinie bedeutet einen Quantensprung für die Sicherheit und Qualität geschlossener Fonds. Bisher konnten sich besonders die schlechten geschlossenen Fonds hinter einer spärlichen Informationspolitik verstecken. Mit der jährlichen Wertermittlungsauflage und zusätzlicher Informationspflicht kommt endlich nachhaltig Licht ins Dunkel. Dies wird eine Menge Emittenten ins Wanken bringen. Ungeklärt ist, wie eine derartige Wertermittlung bei komplexen Blind-Pools stattfinden soll, beispielsweise bei manchen geschlossenen Fonds aus dem Segment Private Equity.</p>
    <p>Der große Sieger ist der Anleger geschlossener Fonds<br>Die geschlossenen Fonds werden nun endgültig salonfähig und verabschieden sich vom Image des grauen Kapitalmarktes. Die jährliche Wertermittlungspflicht wird sich sehr positiv auf die Handelbarkeit der Produkte auswirken. Schon bei der Konstruktion der Fonds werden Emittenten zwangsläufig stärker auf das Thema der Fungibilität achten. Der Gesamtmittelzufluß geschlossener Fonds dürfte bis 2020 sehr stark zunehmen und ein besonders starkes Wachstum erwarte ich für den Umsatz des Zweitmarktes für geschlossene Fonds.</p>
    <a class="more" href="#">Ältere Artikel lesen</a>
  </div>
</article>

<div class="share-bar abs" style="top:1568px">
  <span><svg viewBox="0 0 14 14"><ellipse cx="7" cy="6" rx="6" ry="4.5" fill="#f2d27a"/></svg>Kommentieren <i>0</i></span>
  <span><svg viewBox="0 0 14 14"><circle cx="7" cy="7" r="5" fill="#6fb3de"/></svg>Zwitschern <i>12</i></span>
  <span><svg viewBox="0 0 14 14"><rect x="1" y="1" width="12" height="12" fill="#4a6ea8"/></svg>Teilen <i>0</i></span>
</div>

<article class="post abs" style="top:1613px">
  <div class="post-head"><div class="date-badge"><b>15</b><small>NOV<br>2009</small></div><h2>Sie wollen die besten geschlossenen Fonds finden?</h2></div>
  <div class="post-body">
    <div class="post-image" role="img" aria-label="Bild einer goldenen Krone"></div>
    <p>AIFM Richtlinie für geschlossene Fonds:<br>Auf Nimmerwiedersehen grauer Kapitalmarkt!<br>von Dr. Martin Albrecht am 15. Dezember 2010<br>Die AIFM Richtlinie bedeutet einen Quantensprung für die Sicherheit und Qualität geschlossener Fonds. Bisher konnten sich besonders die schlechten geschlossenen Fonds hinter einer spärlichen Informationspolitik verstecken. Mit der jährlichen Wertermittlungsauflage und zusätzlicher Informationspflicht kommt endlich nachhaltig Licht ins Dunkel. Dies wird eine Menge Emittenten ins Wanken bringen. Ungeklärt ist, wie eine derartige Wertermittlung bei komplexen Blind-Pools stattfinden soll, beispielsweise bei manchen geschlossenen Fonds aus dem Segment Private Equity.</p>
    <p>Der große Sieger ist der Anleger geschlossener Fonds<br>Die geschlossenen Fonds werden nun endgültig salonfähig und verabschieden sich vom Image des grauen Kapitalmarktes. Die jährliche Wertermittlungspflicht wird sich sehr positiv auf die Handelbarkeit der Produkte auswirken. Schon bei der Konstruktion der Fonds werden Emittenten zwangsläufig stärker auf das Thema der Fungibilität achten. Der Gesamtmittelzufluß geschlossener Fonds dürfte bis 2020 sehr stark zunehmen und ein besonders starkes Wachstum erwarte ich für den Umsatz des Zweitmarktes für geschlossene Fonds.</p>
    <a class="more" href="#">Ältere Artikel lesen</a>
  </div>
</article>

<div class="share-bar abs" style="top:2094px">
  <span><svg viewBox="0 0 14 14"><ellipse cx="7" cy="6" rx="6" ry="4.5" fill="#f2d27a"/></svg>Kommentieren <i>0</i></span>
  <span><svg viewBox="0 0 14 14"><circle cx="7" cy="7" r="5" fill="#6fb3de"/></svg>Zwitschern <i>12</i></span>
  <span><svg viewBox="0 0 14 14"><rect x="1" y="1" width="12" height="12" fill="#4a6ea8"/></svg>Teilen <i>0</i></span>
</div>

<h3 class="side-title sidebar abs" style="top:658px">NEWSLETTER</h3>
<form class="newsletter-box abs">
  Seien Sie immer bestens informiert und bestellen Sie meinen Newsletter.
  <label>E-Mail</label>
  <div class="field"></div>
  <div class="send">senden</div>
</form>

<h3 class="side-title sidebar abs" style="top:874px">FINDEN SIE UNS UNTER</h3>
<a class="social-link abs" style="top:917px">
  <svg viewBox="0 0 38 38"><rect x="3" y="9" width="32" height="21" fill="#e4e4e4" stroke="#999"/><path d="M3 9 L19 22 L35 9" fill="none" stroke="#999" stroke-width="1.5"/></svg>E-MAIL</a>
<a class="social-link abs" style="top:982px">
  <svg viewBox="0 0 38 38"><rect x="2" y="2" width="34" height="34" rx="8" fill="#f07a1a"/><circle cx="11" cy="27" r="3" fill="#fff"/><path d="M9 17a12 12 0 0 1 12 12M9 9a20 20 0 0 1 20 20" fill="none" stroke="#fff" stroke-width="3.5"/></svg>RSS FEED</a>
<a class="social-link abs" style="top:1046px">
  <svg viewBox="0 0 38 38"><rect x="3" y="3" width="32" height="32" rx="4" fill="#3b5b9a"/></svg>FREUNDESNETZ</a>
<a class="social-link abs" style="top:1112px">
  <svg viewBox="0 0 38 38"><circle cx="19" cy="19" r="16" fill="#5fb4e0"/></svg>ZWITSCHERPOST</a>

<h3 class="side-title sidebar abs" style="top:1196px">TAG CLOUD</h3>
<div class="tag-cloud abs">
  <span class="s">Lorem</span> <span class="m">ipsum</span> <span class="xs">dolor</span> <span class="s">sit</span> <span class="l">amet</span>, <span class="s">consectetuer adipiscing</span> <span class="xs">elit</span> <span class="xl">Aenean</span> <span class="xs">commodo ligula eget</span> <span class="s">dolor.</span> <span class="s">Cum sociis</span> <span class="m">natoque</span> <span class="s">penatibus et</span> <span class="m">magnis</span> <span class="s">dis parturient montes, nascetur</span> <span class="xl">ridiculus</span> <span class="s">mus.</span> <span class="xs">ut</span> <span class="xl">wisi</span> <span class="s">enim</span> <span class="xs">ad</span> <span class="s">minim</span> <span class="m">veniam</span>, <span class="s">quis nostrud exerci tation</span> <span class="xl">ullamcorper</span> <span class="s">suscipit</span> <span class="m">lobortis</span> <span class="s">nisl ut aliquip ex ea commodo conse-quat.</span>
</div>

<h3 class="side-title sidebar abs" style="top:1531px;border:none">ARCHIV</h3>
<ul class="archive abs">
  <li>Januar 2011 (8)</li><li>Juli 2011 (0)</li>
  <li>Februar 2011 (5)</li><li>August 2011 (0)</li>
  <li>März 2011 (3)</li><li>September 2011 (0)</li>
  <li>April 2011 (10)</li><li>Oktober 2011 (0)</li>
  <li>Mai 2011 (0)</li><li>November 2011 (0)</li>
  <li>Juni 2011 (0)</li><li>Dezember 2011 (0)</li>
</ul>

<footer class="site-footer abs">
  <a href="#">Impressum</a> &nbsp;| &nbsp;<a href="#">Kontakt</a> &nbsp;| &nbsp;<a href="#">AGB</a> | &nbsp;<a href="#">Datenschutz</a>
  <div class="bookmark-badge"></div>
</footer>

</body>
</html>
```